Gutschein-Design für Tätowierer
Zielgruppe
Ich bin ein Tätowierer und suche ein hochwertiges Design, meine Zielgruppe sind Leute jeden Alters
Aufgabenstellung
-Farbe auf meiner Karte sollte wie bei meiner Webseite www.wendelhorst-studio.de sein Pazifikblau/ Marineblau
-Es soll schlicht sein
-mein Logo soll auf die Vorderseite mittig (in schwarz)
-ein Rand soll enthalten sein in einem blauton
-auf die Rückseite sollen Felder zum ausfüllen sein wie zum Beispiel Name, Gutschein wert usw..
-Maße ca. 21 x 10,5 cm

```html
<!DOCTYPE html>
<html lang="de">
<head>
<meta charset="utf-8">
<title>Atelier Wendelhorst Gutschein</title>
<link href="https://fonts.googleapis.com/css2?family=Michroma&display=swap" rel="stylesheet">
<style>
  :root {
    --stage: #141412;
    --card: #f4f4f4;
    --ink: #111111;
    --navy: #24338a;
    --field-line: #6a6a6a;
    --label: #2a2a2a;
    --art-light: #e2e2e2;
    --art-dark: #b9b9b9;
  }
  html, body {
    margin: 0;
    width: 1200px;
    height: 720px;
    overflow: hidden;
    background: var(--stage);
  }
  .stage {
    position: relative;
    width: 1200px;
    height: 720px;
    display: flex;
    align-items: center;
    justify-content: center;
    gap: 60px;
    font-family: "Michroma", sans-serif;
  }
  .card {
    position: relative;
    width: 520px;
    height: 260px;
    background: var(--card);
    box-shadow: 0 10px 30px rgba(0,0,0,0.6);
    overflow: hidden;
  }
  /* Back side: fill-in fields */
  .voucher-art {
    position: absolute;
    right: 18px;
    top: 18px;
    width: 210px;
    height: 170px;
    background: radial-gradient(ellipse at 55% 45%, var(--art-dark), var(--art-light) 70%, transparent 100%);
    opacity: 0.75;
    border-radius: 40% 30% 45% 35%;
  }
  .fields {
    position: absolute;
    left: 26px;
    top: 40px;
    display: flex;
    flex-direction: column;
    gap: 12px;
  }
  .field {
    width: 270px;
    height: 34px;
    border: 1px solid var(--field-line);
    background: rgba(255,255,255,0.4);
    display: flex;
    align-items: center;
    padding-left: 10px;
    font-size: 10px;
    letter-spacing: 0.08em;
    color: var(--label);
    box-sizing: border-box;
  }
  .field:nth-child(2) { margin-left: 30px; }
  .field:nth-child(3) { margin-left: 60px; }
  .field:nth-child(4) { margin-left: 90px; }
  /* Front side: name with blue frame */
  .frame {
    position: absolute;
    inset: 0;
  }
  .brand {
    position: absolute;
    inset: 0;
    display: flex;
    align-items: center;
    justify-content: center;
  }
  .brand-name {
    font-size: 22px;
    color: var(--ink);
    letter-spacing: 0.06em;
    white-space: nowrap;
  }
</style>
</head>
<body>
<main class="stage">
  <section class="card card--back" aria-label="Gutschein Rückseite">
    <div class="voucher-art" role="img" aria-label="Zeichnung einer Hand mit Tätowiermaschine in hellem Grau"></div>
    <div class="fields">
      <div class="field">GUTSCHEIN</div>
      <div class="field">NAME</div>
      <div class="field">WERT</div>
      <div class="field">VON</div>
    </div>
  </section>

  <section class="card card--front" aria-label="Gutschein Vorderseite">
    <svg class="frame" viewBox="0 0 520 260" aria-hidden="true">
      <path d="M30 8 L505 22 L503 30 L40 20 Z" fill="var(--navy)"/>
      <path d="M20 236 L500 244 L498 254 L25 248 Z" fill="var(--navy)"/>
      <path d="M12 25 L28 18 L32 240 L10 250 Z" fill="var(--navy)"/>
      <path d="M488 30 L510 26 L512 252 L492 246 Z" fill="var(--navy)"/>
    </svg>
    <div class="brand">
      <span class="brand-name">Atelier Wendelhorst</span>
    </div>
  </section>
</main>
</body>
</html>
```